Corvell Ashbright Website

Updated website for Corvell Ashbright Dry Cleaners & Garment Care.

Please look at www.tindalefabricare.example we really like this site!!!

We are not set on colors or fonts. Looking for an professional easy to use site that looks and works even better on a mobile device. 90% of our customers visit us on cell phones.

Target Market(s)

We are located in an up scale area with young trendy individuals but, also very successful mature customers as well. Probably geared more to tech savvy younger crowd.

Industry/Entity Type

Dry Cleaning

Coding

Font styles to use
Serif
Script

Colors
85abd2
85cae6
cee9f5
cfdeed
757575

Requirements
Must have
• Must look good on a mobile device and have sign up for our pick up and delivery. Geographical pick up and delivery perimeters would be great as well. Capturing emails and other user data for future marketing. We do a lot of advertising.
• Please look at www.tindalefabricare.example we really like this site!!!
• Search engine optimized.
• Also we are adding a new POS system that will have a login for customers and possibly an app.
Nice to have
• 100% satisfaction guaranteed and scrolling reviews somewhere on the page.

```html
<!DOCTYPE html>
<html lang="en">
<head>
<meta charset="utf-8">
<title>Corvell Ashbright – Complimentary Pick Up &amp; Delivery</title>
<link href="https://fonts.googleapis.com/css2?family=Source+Sans+3:wght@400;600;700&display=swap" rel="stylesheet">
<style>
  :root {
    --navy: #14296b;
    --ink: #1c1c1c;
    --text: #2b2b2b;
    --muted: #6b6b6b;
    --band: #f2f2f2;
    --white: #ffffff;
    --line: #e3e3e3;
    --field-border: #c9c9c9;
    --required: #d0312d;
  }
  * { box-sizing: border-box; margin: 0; padding: 0; }
  html, body { width: 1200px; height: 678px; overflow: hidden; }
  body {
    position: relative;
    background: var(--white);
    font-family: "Source Sans 3", "Source Sans Pro", sans-serif;
    color: var(--text);
  }
  .site-header {
    position: absolute; left: 0; top: 0; width: 1200px; height: 81px;
    background: var(--white);
    box-shadow: 0 2px 4px rgba(0,0,0,0.12);
    z-index: 2;
  }
  .brand {
    position: absolute; left: 150px; top: 0; width: 134px; height: 114px;
    background: var(--navy);
    display: flex; flex-direction: column; align-items: center; justify-content: flex-end;
    padding-bottom: 18px;
    z-index: 3;
  }
  .brand-dot {
    width: 44px; height: 44px; border-radius: 50%;
    background: var(--white); margin-bottom: 14px;
  }
  .brand-name {
    color: var(--white); font-weight: 700; font-size: 9px; letter-spacing: 0.3px;
    text-transform: uppercase;
  }
  .contact-strip {
    position: absolute; left: 765px; top: 0; width: 291px; height: 28px;
    border-bottom: 1px solid var(--line);
    font-size: 9.5px; color: var(--muted);
    display: flex; align-items: center; gap: 20px; padding-left: 12px;
  }
  .contact-strip .address { display: flex; align-items: center; gap: 4px; }
  .contact-strip .phone { color: var(--ink); }
  .main-nav {
    position: absolute; top: 35px; left: 454px; height: 39px;
    display: flex; align-items: center;
  }
  .main-nav a {
    color: var(--text); text-decoration: none; font-size: 12px;
    letter-spacing: 1px; text-transform: uppercase; margin-right: 25px;
  }
  .cta-button {
    position: absolute; left: 886px; top: 35px; width: 170px; height: 39px;
    background: var(--navy); color: var(--white);
    display: flex; align-items: center; justify-content: center;
    font-size: 12.5px; font-weight: 700; letter-spacing: 1.6px; text-transform: uppercase;
  }
  .intro {
    position: absolute; left: 0; top: 81px; width: 1200px; height: 377px;
    background: var(--band); text-align: center;
  }
  .intro h1 {
    margin-top: 50px; font-size: 30px; font-weight: 700; color: var(--ink);
  }
  .intro p {
    width: 540px; margin: 0 auto; font-size: 13.5px; line-height: 20px;
  }
  .intro .lead { margin-top: 18px; }
  .intro p + p { margin-top: 20px; }
  .signup-form { position: absolute; left: 286px; top: 543px; width: 622px; }
  .field label {
    display: block; text-align: center; font-size: 13px; font-weight: 700;
    color: var(--ink); margin-bottom: 6px;
  }
  .field label .req { color: var(--required); }
  .field .input {
    height: 28px; border: 1px solid var(--field-border); border-radius: 2px;
    background: var(--white);
  }
  .form-divider { height: 1px; background: var(--line); margin: 17px 0 21px; }
  .field-row { display: flex; gap: 13px; }
  .field-row .field { flex: 1; }
</style>
</head>
<body>
  <header class="site-header">
    <div class="contact-strip">
      <span class="address">
        <svg width="10" height="9" viewBox="0 0 10 9" aria-hidden="true"><path d="M5 0 L10 4.5 H8.5 V9 H6 V6 H4 V9 H1.5 V4.5 H0 Z" fill="#8a8a8a"/></svg>
        218 Linden Ridge Rd, Ashbright, MN 55400
      </span>
      <span class="phone">(555) 014-2290</span>
    </div>
    <nav class="main-nav">
      <a href="#">Home</a>
      <a href="#">About</a>
      <a href="#">Our Services</a>
      <a href="#">Coverage Area</a>
      <a href="#">Contact Us</a>
    </nav>
    <a class="cta-button">Schedule Pickup</a>
  </header>

  <div class="brand">
    <span class="brand-dot"></span>
    <span class="brand-name">Corvell Ashbright</span>
  </div>

  <section class="intro">
    <h1>Complimentary Pick Up &amp; Delivery</h1>
    <p class="lead">As a new customer, when you sign up for our FREE Pick Up and Delivery service, you will receive 25% off your first month's bill.</p>
    <p>Enjoy the convenience of our complimentary pickup and delivery service right to your home or office. Life can be stressful enough; don’t add another errand to your list. We Pick up and deliver every Monday and Thursday. Simply call or fill out the information below to sign up.</p>
    <p>Once signed up, you will receive a confirmation email that we have received your request. A follow up email will be sent, within 24 hours, advising you of your first pick up date. Typically, your initial pickup will be scheduled for the first Monday or Thursday after we received your request.</p>
  </section>

  <form class="signup-form">
    <div class="field">
      <label>Full Name <span class="req">*</span></label>
      <div class="input"></div>
    </div>
    <div class="form-divider"></div>
    <div class="field-row">
      <div class="field">
        <label>Suite, Unit, App <span class="req">*</span></label>
        <div class="input"></div>
      </div>
      <div class="field">
        <label>Street <span class="req">*</span></label>
        <div class="input"></div>
      </div>
    </div>
  </form>
</body>
</html>
```